CV Template

We need a graphic design to our new CV templates for our consultants. We are a small young Danish upcoming IT-business company making software solutions for our customers etc. You can visit our new website here: dev.solbakken-data.com, then you can see our web design, colors etc. I have attached a file for your inspiration :-) In the presentation I would like to have a picture of the employee, some text who descripe the profile/consultant and then I imagine that there is a table where we can write the employee's skills etc.

I would like the design to be "fresh & catchy" :-)

Looking forward to hear from you.

Best regards,
Birgit

```html
<!DOCTYPE html>
<html lang="da">
<head>
<meta charset="utf-8">
<title>CV – Jonas Kjærgaard</title>
<link href="https://fonts.googleapis.com/css2?family=Open+Sans:wght@400;600;700&display=swap" rel="stylesheet">
<style>
  :root{
    --page-bg:#e9edf5;
    --panel:#ffffff;
    --blue:#1f6fc0;
    --dot:#2f6fc4;
    --ink:#111111;
    --muted:#444444;
    --rule:#7ea3d3;
    --brand:#4d5a70;
    --letter:#f5b400;
    --lvl1:#fde5cf;
    --lvl2:#fdc894;
    --lvl3:#fdbd7f;
    --lvl4:#fdae66;
    --lvl5:#fb9405;
  }
  *{margin:0;padding:0;box-sizing:border-box}
  html,body{width:902px;height:1200px;overflow:hidden}
  body{background:var(--page-bg);font-family:"Open Sans",Arial,sans-serif;color:var(--ink);position:relative}
  .abs{position:absolute}
  .photo{left:121px;top:45px;width:213px;height:213px;border-radius:50%;background:radial-gradient(circle at 50% 40%,#d8cbbf 0,#a9a49d 45%,#7d8078 100%)}
  .panel{left:65px;top:216px;width:796px;height:910px;background:var(--panel);border-radius:46px}
  .brand{right:34px;top:42px;text-align:right;color:var(--brand)}
  .brand-name{font-size:21px;font-weight:400;letter-spacing:1.5px;line-height:1}
  .brand-tag{font-size:7.5px;letter-spacing:.6px;text-transform:uppercase;margin-top:5px}
  .name{left:380px;top:98px;font-size:31px;font-weight:700;letter-spacing:-1px;line-height:1}
  .role{left:380px;top:145px;font-size:17.5px;line-height:25px;width:300px}
  .sec-title{color:var(--blue);font-weight:700;font-size:17.5px;line-height:1;letter-spacing:-.2px}
  .sec-rule{height:1px;background:var(--rule)}
  .left-text{left:70px;width:262px;text-align:right;font-size:12px;line-height:17.6px;color:var(--muted);letter-spacing:-.1px}
  .fact{width:150px;text-align:center}
  .fact .dot{width:96px;height:96px;border-radius:50%;background:var(--dot);margin:0 auto 10px}
  .fact h3{color:var(--blue);font-size:14.5px;font-weight:700;margin-bottom:6px}
  .fact p{font-size:12px;line-height:17.8px;color:var(--muted)}
  .projects-title{left:70px;width:262px;text-align:right;top:688px;color:var(--blue);font-size:12px;font-weight:700}
  .project{left:80px;width:262px;font-size:12px;line-height:17px;padding-left:19px}
  .project b{position:absolute;left:0;top:-2px;color:var(--letter);font-size:15px}
  .lvl-head{top:568px;height:90px;writing-mode:vertical-rl;transform:rotate(180deg);font-size:11px;white-space:nowrap;text-align:left}
  .col-head{font-size:12px}
  .band{display:flex}
  .band span{width:37px;height:100%}
  .band span:nth-child(1){background:var(--lvl1)}
  .band span:nth-child(2){background:var(--lvl2)}
  .band span:nth-child(3){background:var(--lvl3)}
  .band span:nth-child(4){background:var(--lvl4)}
  .band span:nth-child(5){background:var(--lvl5)}
  .cat{left:370px;color:var(--blue);font-size:12px;font-weight:700}
  .skill{left:340px;width:120px;text-align:right;font-size:12px;line-height:16.5px}
  .years{left:680px;width:26px;text-align:center;font-size:12px;line-height:16.5px}
  .vline{left:735px;width:1px;background:#222}
  .sum-label{left:300px;width:235px;text-align:right;color:var(--blue);font-size:11.5px;font-weight:600}
  .sum-val{left:551px;width:290px;font-size:11.5px;line-height:16.3px}
  .footer{top:1136px;font-size:11.5px}
</style>
</head>
<body>
  <div class="abs photo" role="img" aria-label="Portrætfoto af konsulenten"></div>

  <div class="abs brand">
    <div class="brand-name">SOLBAKKEN DATA</div>
    <div class="brand-tag">Kompetente løsninger til alle</div>
  </div>

  <h1 class="abs name">JONAS KJÆRGAARD</h1>
  <p class="abs role">Rutineret og erfaren Software udvikler &amp; konsulent</p>

  <div class="abs panel"></div>

  <h2 class="abs sec-title" style="left:70px;width:262px;text-align:right;top:253px">Profilbeskrivelse</h2>
  <div class="abs sec-rule" style="left:75px;width:257px;top:275px"></div>
  <p class="abs left-text" style="top:279px">Erfaren software udvikler med 25 års erfaring, som selvstændig hvor han bl.a. har arbejdet med udvikling af kundespecifikke applikationer til VOS til WEB i samarbejde med kunder/ brugere. Derudover stor erfaring med analyse, design, programmering, test, uddannelse/ undervisning, kundesupport og projektledelse. Ud over at være en dygtig software udvikler er han også en stabil og rutineret konsulent, som er vant til, at yde konsulentbistand, support og udvikling af softwareløsninger til VOS, Pingvin OS og WEB.</p>

  <div class="abs fact" style="left:367px;top:248px">
    <div class="dot"></div>
    <h3>Uddannelse</h3>
    <p>Uddannet som datalog/cand. scient ved Øresund Universitet februar 1989, hovedfag datalogi, bifag matematik</p>
  </div>
  <div class="abs fact" style="left:521px;top:248px">
    <div class="dot"></div>
    <h3>Certificeringer</h3>
    <p>Ingen certificeringer</p>
  </div>
  <div class="abs fact" style="left:673px;top:248px">
    <div class="dot"></div>
    <h3>Sprog</h3>
    <p>Dansk: Modersmål i både tale- og skrift</p>
    <p style="margin-top:10px">Engelsk: Behersker det i både tale- og skrift</p>
  </div>

  <h2 class="abs sec-title" style="left:70px;width:262px;text-align:right;top:533px">Erhvervs erfaringer</h2>
  <div class="abs sec-rule" style="left:75px;width:257px;top:556px"></div>
  <p class="abs left-text" style="top:561px">Været selvstændig i 25 år med egen virksomhed hvor forretningsområdet primært bestod i udvikling af kundespecifikke applikationer til VOS, Pingvin OS og WEB primært baseret på Visual Grund, ASX, Kaffe, HTX, KvartsSQL, LyngSQL, Orakeldata, Arkivbase, Paralex.</p>

  <h3 class="abs projects-title">Eksempler på udviklingsprojekter</h3>
  <p class="abs project" style="top:719px"><b>A</b>WEB-baseret pakkelistesystem til Nordcem med mulighed for leverandørregistreringer og opfølgning (shipping/ expediting) hos Nordcem. Tilsvarende system udviklet til Katalysegruppen.</p>
  <p class="abs project" style="top:839px"><b>B</b>Kørselsregistreringssystem udviklet i Visual Grund som Vindue-applikation til Værnfælles Logistik.</p>
  <p class="abs project" style="top:909px"><b>C</b>Beregnings- og administrationsprogrammer til De Nordiske Brevdueklubber (i dag også anvendt i Sverige og Norge), dels som Vindue-applikationer, dels WEB på Pingvin-server.</p>

  <h2 class="abs sec-title" style="left:360px;top:533px">Kompetenceområder</h2>
  <div class="abs sec-rule" style="left:360px;width:482px;top:556px"></div>

  <div class="abs lvl-head" style="left:478px">Begynder niveau</div>
  <div class="abs lvl-head" style="left:515px">Basisniveau</div>
  <div class="abs lvl-head" style="left:552px">Professionel</div>
  <div class="abs lvl-head" style="left:589px">Supervisoniveau</div>
  <div class="abs lvl-head" style="left:626px">Ekspertniveau</div>
  <div class="abs col-head" style="left:661px;top:650px">Års erfaring</div>
  <div class="abs col-head" style="left:742px;top:634px;line-height:16px">Sidst<br>&nbsp;anvendt</div>

  <div class="abs cat" style="top:666px">Database Administration</div>
  <div class="abs band" style="left:468px;top:682px;height:99px"><span></span><span></span><span></span><span></span><span></span></div>
  <div class="abs skill" style="top:682px">KvartsSQL<br>LyngSQL<br>Orakeldata<br>Arkivbase<br>Paralex<br>Implementering</div>
  <div class="abs years" style="top:682px">9<br>9<br>9<br>3<br>8</div>
  <div class="abs vline" style="top:682px;height:98px"></div>

  <div class="abs cat" style="top:782px">Programmeringssprog</div>
  <div class="abs band" style="left:468px;top:798px;height:83px"><span></span><span></span><span></span><span></span><span></span></div>
  <div class="abs skill" style="top:798px">Skarp<br>Visual Grund<br>Kaffe<br>VGScript<br>HTX</div>
  <div class="abs years" style="top:798px">7<br>3<br>4<br>5<br>7</div>
  <div class="abs vline" style="top:798px;height:83px"></div>

  <div class="abs cat" style="top:881px">Andre</div>
  <div class="abs band" style="left:468px;top:898px;height:66px"><span></span><span></span><span></span><span></span><span></span></div>
  <div class="abs skill" style="top:898px">Projektledelse<br>System drift/<br>Administration<br>Webservice</div>
  <div class="abs years" style="top:898px">7<br>4<br><br>5</div>
  <div class="abs vline" style="top:898px;height:66px"></div>

  <div class="abs sec-rule" style="left:360px;width:482px;top:982px"></div>

  <div class="abs sum-label" style="top:1003px">Primære udviklingssprog:</div>
  <div class="abs sum-val" style="top:1003px">Skarp, Visual Grund, Kaffe, VGScript, HTX</div>
  <div class="abs sum-label" style="top:1019px">Primære udviklingsværktøjer:</div>
  <div class="abs sum-val" style="top:1019px">Skarp, HTX, WebScript, ASX, VG, KvartsSQL, LyngSQL,<br>Arkivbase.<br>Derudover kendskab til: Plus, Trin.</div>
  <div class="abs sum-label" style="top:1068px">Databaseerfaring:</div>
  <div class="abs sum-val" style="top:1068px">KvartsSQL, LyngSQL, Orakeldata, Arkivbase, Paralex.</div>
  <div class="abs sum-label" style="top:1084px">Miljøer:</div>
  <div class="abs sum-val" style="top:1083px;font-size:12.5px">Vindue OS, WEB, Pingvin Server/HTX, WebVært/ASX.</div>

  <footer>
    <span class="abs footer" style="left:108px">Solbakken ApS</span>
    <span class="abs footer" style="left:220px">Lindeallé 14</span>
    <span class="abs footer" style="left:328px">2200 København N.</span>
    <span class="abs footer" style="left:469px">Tel: +45 70 12 34 56</span>
    <span class="abs footer" style="left:614px">www.solbakken-data.dk</span>
  </footer>
</body>
</html>
```